Application for baby milk and water counter

We are building baby food app. Need to design main screen for tha app first so we can go forward to other secondary screens of the app

Food dashboard screen
Food dashboard screen is main page for view/edit food data

General vision
I see the app in pastel colors with some illustrations to make the app more in positive. You can influence from game Lantern Hollow. I see with smooth colors and gradients like in a game. Also need to have animations/transitions for each action. Each click should create smooth transition to new state. My idea is to build one dashboard screen for food which we can reuse it for other screens. So a lot of thinking should go into design stage to app appealing.

Food Dashboard
Current screen should show all the data about food intake of the baby. So here user should see

Milk How much food baby had in ml/oz. So there should be some kind of illustrated bottle or glass or smth that shows it is filled with that amount.

Add/Remove controls for food. Should be some kind of custom control for inputing amount to remove/add. I see it as a slider on the side of the bottle. User slides up or down and amount is added/removed.

Notification. So user should be aware how many hours/minutes left for next food intake. This is optional field, so consider it could be disabled. So no empty space should be on a screen. There should be human readable text. Something like. 1:30 minutes left for next intake. Maybe could be some custom made icons to illustrate that it is next food intake.

Burped: User should have ability to how much baby burped. This amount is integer value. So it could be “Baby burped 2 times today”. So again here I see some custom made/icon to illustrate how many times baby burped and amount next to it. I see changing the value just by tapping, but I don’t know how to edit if user tapped accidentally more than it should be. So TBD here.

Date and time: Dashboard should show for which date it is viewing/editing data. Should be able to change it, so user can add/edit data for yesterday. Don’t want to see here calendar on a screen so need to come up with nice design decision.

Water: User should have ability to view/edit water intake of the baby, but water is secondary information so it should be smaller than milk, or come up with some other idea how to show the water. I see to have same controls for water like for milk. Water intake is optional it can be disabled by the user.

Target Market(s)

For just became mothers

Font styles to use
Sans Serif

Colors
0094D4
00A9DD
6FCCEA
C7EBF8
E9F6FB
FFC000
F8CF3A
FAE287
FDF2CF
FEFAEE
E54698
E96AAD
F1A4CE
F9D9EA
FCEFF6

Requirements
Must have
• Ilustrations or playfull icons for show information

```html
<!DOCTYPE html>
<html lang="en">
<head>
<meta charset="utf-8">
<title>Baby Food Dashboard</title>
<link href="https://fonts.googleapis.com/css2?family=Lato:wght@400;700;900&display=swap" rel="stylesheet">
<style>
  :root {
    --blue-deep: #0094D4;
    --blue: #00A9DD;
    --blue-mid: #6FCCEA;
    --blue-soft: #C7EBF8;
    --blue-pale: #E9F6FB;
    --notice: #A9DCF0;
    --ink: #1d1d1f;
    --ink-soft: #4a4a4a;
    --muted: #c8c8c8;
    --line: #b9bec3;
    --stage: #eef2f5;
    --screen: #ffffff;
  }
  * { box-sizing: border-box; margin: 0; padding: 0; }
  html, body { width: 1200px; height: 666px; overflow: hidden; }
  body {
    background: var(--stage);
    font-family: "Lato", sans-serif;
    color: var(--ink);
    position: relative;
  }
  .app-screen {
    position: absolute;
    left: 454px; top: 17px;
    width: 234px; height: 505px;
    transform: scale(1.25);
    transform-origin: top left;
    background: var(--screen);
    border-radius: 22px;
    overflow: hidden;
  }
  .status-bar {
    position: absolute; left: 16px; right: 18px; top: 8px;
    display: flex; justify-content: space-between; align-items: center;
    font-size: 8px; font-weight: 700;
  }
  .status-icons { display: flex; gap: 4px; align-items: center; }

  .picker {
    position: absolute; top: 52px; width: 108px; height: 28px;
    border: 1px solid var(--line); border-radius: 5px;
    display: flex; align-items: center; gap: 6px; padding-left: 8px;
  }
  .picker--date { left: 3px; border-color: var(--blue); }
  .picker--time { left: 123px; }
  .picker-label { font-size: 5.5px; color: var(--ink-soft); line-height: 1.2; }
  .picker-value { font-size: 6px; font-weight: 700; line-height: 1.2; }

  .intake-option {
    position: absolute; top: 107px;
    display: flex; align-items: center; gap: 6px;
    font-size: 11px; font-weight: 700;
  }
  .intake-option--milk { left: 20px; }
  .intake-option--water { left: 138px; color: var(--muted); }
  .radio {
    width: 9px; height: 9px; border-radius: 50%;
    border: 1px solid var(--blue); display: grid; place-items: center;
  }
  .radio--on::after { content: ""; width: 5px; height: 5px; border-radius: 50%; background: var(--blue); }
  .radio--off { border-color: var(--muted); }

  .bottle-art { position: absolute; border-radius: 10px 10px 14px 14px; }
  .bottle-art--milk {
    left: 17px; top: 145px; width: 64px; height: 152px;
    background: linear-gradient(180deg, #f6d27a 0%, #f6d27a 14%, #6fb6e6 14%, #6fb6e6 26%, #f3ecd9 26%, #e7ddc2 100%);
  }
  .bottle-art--water {
    left: 135px; top: 133px; width: 70px; height: 167px; opacity: .7;
    background: linear-gradient(180deg, #f5f5f5 0%, #f7e3c4 14%, #a8e2dc 26%, var(--blue-soft) 40%, var(--blue-pale) 100%);
  }
  .scale {
    position: absolute; list-style: none;
    font-size: 4.6px; line-height: 6.6px; text-align: left;
  }
  .scale--milk { left: 84px; top: 197px; color: var(--ink); }
  .scale--milk li:first-child, .scale--milk li:nth-child(2) { color: #9a9a9a; }
  .scale--water { left: 213px; top: 210px; color: #9a9a9a; line-height: 6.4px; }

  .amount { position: absolute; top: 311px; width: 90px; text-align: center; }
  .amount--milk { left: 5px; }
  .amount--water { left: 123px; color: var(--muted); }
  .amount-value { font-size: 11.5px; font-weight: 700; letter-spacing: .2px; }
  .amount-caption { font-size: 7px; margin-top: 1px; }

  .burp-card {
    position: absolute; left: 9px; top: 359px; width: 207px; height: 67px;
    border: 1px solid var(--line); border-radius: 5px;
  }
  .burp-step { position: absolute; left: 19px; font-size: 8px; color: var(--ink-soft); }
  .burp-step--up { top: 7px; }
  .burp-step--down { top: 44px; }
  .burp-count {
    position: absolute; left: 10px; top: 24px; width: 20px; height: 20px;
    background: var(--blue-deep); color: #fff; border-radius: 2px;
    display: grid; place-items: center; font-size: 8px; font-weight: 700;
  }
  .burp-label { position: absolute; left: 37px; top: 30px; font-size: 7.5px; color: var(--ink-soft); }
  .burp-divider { position: absolute; left: 110px; top: 8px; width: 1px; height: 51px; background: var(--blue-mid); }
  .burp-total-label { position: absolute; left: 126px; top: 15px; font-size: 7.5px; color: var(--ink-soft); }
  .burp-total {
    position: absolute; left: 127px; top: 27px; width: 53px; height: 22px;
    border: 1px solid var(--blue); border-radius: 3px;
    display: grid; place-items: center; font-size: 8.5px; font-weight: 700;
  }

  .next-intake {
    position: absolute; left: 9px; top: 447px; width: 207px; height: 34px;
    background: var(--notice); border: 1px solid var(--blue-mid); border-radius: 4px;
    display: flex; align-items: center; gap: 13px; padding-left: 11px;
    font-size: 8px; font-weight: 700;
  }
  .toggle {
    width: 22px; height: 11px; border-radius: 6px; background: #fff;
    border: 1px solid var(--blue-mid); position: relative;
  }
  .toggle::after {
    content: ""; position: absolute; right: 2px; top: 1.5px;
    width: 7px; height: 7px; border-radius: 50%; background: var(--blue-deep);
  }
</style>
</head>
<body>
  <main class="app-screen">
    <header class="status-bar">
      <span class="status-time">9:41</span>
      <span class="status-icons">
        <svg width="9" height="7" viewBox="0 0 9 7"><path d="M4.5 7 L0.5 2.5 A6 6 0 0 1 8.5 2.5 Z" fill="#1d1d1f"/></svg>
        <svg width="12" height="6" viewBox="0 0 12 6"><rect x="0.5" y="0.5" width="10" height="5" rx="1.2" fill="none" stroke="#1d1d1f"/><rect x="1.5" y="1.5" width="8" height="3" fill="#1d1d1f"/><rect x="11" y="2" width="1" height="2" fill="#1d1d1f"/></svg>
      </span>
    </header>

    <div class="picker picker--date">
      <svg width="9" height="9" viewBox="0 0 9 9"><rect x="0.5" y="1.5" width="8" height="7" rx="1" fill="none" stroke="#1d1d1f" stroke-width=".8"/><line x1="0.5" y1="3.5" x2="8.5" y2="3.5" stroke="#1d1d1f" stroke-width=".8"/><line x1="2.5" y1="0.5" x2="2.5" y2="2.5" stroke="#1d1d1f" stroke-width=".8"/><line x1="6.5" y1="0.5" x2="6.5" y2="2.5" stroke="#1d1d1f" stroke-width=".8"/></svg>
      <div><p class="picker-label">Date</p><p class="picker-value">June 05, 2023</p></div>
    </div>
    <div class="picker picker--time">
      <svg width="9" height="9" viewBox="0 0 9 9"><circle cx="4.5" cy="4.5" r="4" fill="none" stroke="#1d1d1f" stroke-width=".8"/><path d="M4.5 2.2 V4.6 L6 5.6" fill="none" stroke="#1d1d1f" stroke-width=".8"/></svg>
      <div><p class="picker-label">Time</p><p class="picker-value">12:30 PM</p></div>
    </div>

    <div class="intake-option intake-option--milk"><span class="radio radio--on"></span>Milk</div>
    <div class="intake-option intake-option--water"><span class="radio radio--off"></span>Water</div>

    <div class="bottle-art bottle-art--milk" role="img" aria-label="Illustrated baby bottle filled with milk"></div>
    <ul class="scale scale--milk">
      <li>220</li><li>200</li><li>180</li><li>160</li><li>140</li><li>120</li><li>100</li><li>80</li><li>60</li><li>40</li><li>20</li><li>00</li>
    </ul>
    <div class="bottle-art bottle-art--water" role="img" aria-label="Illustrated sippy bottle with handles for water"></div>
    <ul class="scale scale--water">
      <li>220</li><li>200</li><li>180</li><li>160</li><li>140</li><li>120</li><li>100</li><li>80</li><li>60</li><li>40</li><li>20</li><li>00</li>
    </ul>

    <div class="amount amount--milk"><p class="amount-value">180 ML</p><p class="amount-caption">Remaining</p></div>
    <div class="amount amount--water"><p class="amount-value">00 ML</p><p class="amount-caption">Remaining</p></div>

    <section class="burp-card">
      <span class="burp-step burp-step--up">+</span>
      <span class="burp-count">2</span>
      <span class="burp-label">Times Burped</span>
      <span class="burp-step burp-step--down">-</span>
      <span class="burp-divider"></span>
      <span class="burp-total-label">Total Burped</span>
      <span class="burp-total">08</span>
    </section>

    <div class="next-intake">
      <span class="toggle"></span>
      <span>2 hours left for next intake</span>
    </div>
  </main>
</body>
</html>
```